Business Cards and Stationery for Mechanical Contractor
Stalwart Ductworks Contractors, Inc.
Business Cards and Stationery for Mechanical Contractor - Construction
Creative Brief
Professional
Howard Pelley
President
3148 Foundry Ave. Fort Wayne, IN 46139
hpelley@stalwartducts.example
www.StalwartDucts.example

```html
<!DOCTYPE html>
<html lang="en">
<head>
<meta charset="utf-8">
<title>Stalwart Ductworks Contractors, Inc. — Business Card</title>
<link rel="stylesheet" href="https://fonts.googleapis.com/css2?family=Montserrat:wght@400;600;700&display=swap">
<style>
  :root {
    --bg: #e9e6e1;
    --card-white: #ffffff;
    --brand-green: #2f9a4c;
    --brand-green-dark: #23803c;
    --green-accent: #45ad5f;
    --swoosh-grey: #4a4a4a;
    --swoosh-light: #bdbdbd;
    --text-white: #ffffff;
  }
  * { box-sizing: border-box; margin: 0; padding: 0; }
  html, body { width: 1200px; height: 1023px; overflow: hidden; }
  body {
    background: var(--bg);
    font-family: "Montserrat", sans-serif;
    position: relative;
  }
  .business-card {
    position: absolute;
    left: 190px;
    width: 820px;
    height: 469px;
    overflow: hidden;
    box-shadow: 0 10px 30px rgba(0,0,0,0.18);
  }
  .card-back { top: 28px; background: var(--brand-green); }
  .card-front { top: 526px; background: var(--card-white); }
  .card-shapes { position: absolute; inset: 0; width: 100%; height: 100%; }

  .brand-lockup {
    position: absolute;
    display: flex;
    align-items: center;
    gap: 15px;
  }
  .brand-mark { width: 38px; height: 38px; border-radius: 50%; flex: none; }
  .brand-name {
    font-weight: 700;
    font-size: 20px;
    line-height: 1.2;
    letter-spacing: 0.4px;
    text-transform: uppercase;
  }
  .card-back .brand-lockup { left: 50%; top: 50%; transform: translate(-50%, -50%); }
  .card-back .brand-mark { background: var(--text-white); }
  .card-back .brand-name { color: var(--text-white); }
  .card-front .brand-lockup { left: 90px; top: 140px; }
  .card-front .brand-mark { background: var(--brand-green); }
  .card-front .brand-name { color: var(--brand-green-dark); }

  .contact-block {
    position: absolute;
    left: 600px;
    top: 178px;
    width: 205px;
    color: var(--text-white);
  }
  .person-name { font-weight: 700; font-size: 19px; }
  .person-title {
    font-weight: 400; font-size: 9.5px;
    letter-spacing: 3px; text-transform: uppercase;
    margin-top: 2px;
  }
  .address { font-size: 10.5px; line-height: 1.5; margin-top: 12px; }
  .contact-list { list-style: none; margin-top: 16px; }
  .contact-item {
    display: flex; align-items: center; gap: 9px;
    font-size: 10.5px; margin-bottom: 11px;
    white-space: nowrap;
  }
  .contact-icon { width: 12px; height: 12px; flex: none; }
</style>
</head>
<body>
  <section class="business-card card-back" aria-label="Business card back">
    <svg class="card-shapes" viewBox="0 0 1000 571" preserveAspectRatio="none" aria-hidden="true">
      <path d="M1000 0 L870 0 C820 60 760 110 690 150 C820 120 920 70 1000 20 Z" fill="var(--green-accent)"/>
    </svg>
    <div class="brand-lockup">
      <span class="brand-mark"></span>
      <p class="brand-name">Stalwart Ductworks<br>Contractors, Inc.</p>
    </div>
  </section>

  <section class="business-card card-front" aria-label="Business card front">
    <svg class="card-shapes" viewBox="0 0 1000 571" preserveAspectRatio="none" aria-hidden="true">
      <path d="M1000 0 L880 0 C700 190 430 430 0 500 L0 571 L1000 571 Z" fill="var(--brand-green)"/>
      <path d="M1000 0 L950 0 C760 170 470 395 0 472 C480 418 790 220 905 0 Z" fill="var(--swoosh-light)" opacity="0.7"/>
      <path d="M880 0 L905 0 C770 220 480 430 0 500 L0 492 C440 420 700 200 880 0 Z" fill="var(--swoosh-grey)"/>
    </svg>

    <div class="brand-lockup">
      <span class="brand-mark"></span>
      <p class="brand-name">Stalwart Ductworks<br>Contractors, Inc.</p>
    </div>

    <div class="contact-block">
      <p class="person-name">Howard Pelley</p>
      <p class="person-title">President</p>
      <p class="address">3148 Foundry Ave.<br>Fort Wayne, IN 46139</p>
      <ul class="contact-list">
        <li class="contact-item">
          <svg class="contact-icon" viewBox="0 0 16 16"><path d="M3 1h3l1.5 4-2 1.2a9 9 0 0 0 4.3 4.3L11 8.5l4 1.5v3a2 2 0 0 1-2 2C7 15 1 9 1 3a2 2 0 0 1 2-2z" fill="#fff"/></svg>
          <span>260.555.0148</span>
        </li>
        <li class="contact-item">
          <svg class="contact-icon" viewBox="0 0 16 16"><rect x="2" y="6" width="12" height="8" rx="1" fill="#fff"/><rect x="4" y="1" width="8" height="5" fill="#fff"/></svg>
          <span>260.555.0149</span>
        </li>
        <li class="contact-item">
          <svg class="contact-icon" viewBox="0 0 16 16"><rect x="4" y="1" width="8" height="14" rx="1.5" fill="#fff"/></svg>
          <span>260.555.0172</span>
        </li>
        <li class="contact-item">
          <svg class="contact-icon" viewBox="0 0 16 16"><rect x="1" y="3" width="14" height="10" rx="1" fill="#fff"/><path d="M1 4l7 5 7-5" stroke="var(--brand-green)" stroke-width="1.4" fill="none"/></svg>
          <span>hpelley@stalwartducts.example</span>
        </li>
        <li class="contact-item">
          <svg class="contact-icon" viewBox="0 0 16 16"><circle cx="8" cy="8" r="6.5" stroke="#fff" stroke-width="1.5" fill="none"/><path d="M1.5 8h13M8 1.5c-3 3.5-3 9.5 0 13M8 1.5c3 3.5 3 9.5 0 13" stroke="#fff" stroke-width="1.2" fill="none"/></svg>
          <span>www.StalwartDucts.example</span>
        </li>
      </ul>
    </div>
  </section>
</body>
</html>
```